Business card

We need a business card design for our company based in Auckland , New Zealand called 'Kestrel + Design Ltd'. We provide architectural services. We would like to see designs that use the max. three colours (such as white, black, grey) The final design should communicate financial safety and growth."
Also I will provide our company logo. I would like to the logo to be embeded onto our business card.

Target Market(s)

new residential house, alteration & addition & light commericila design & drafting service

Industry/Entity Type

Architecture

Contact Information for Business Card

Company name: kestrel + design Ltd.
Name: Mark Telford
Job title: architectural designer & Design RQC
email address: mark@kdstudio.co.nz
mobile number: 02 5319 6620
web site: www.kdstudio.co.nz

Requirements
Must have
• My project must have..
• - embeded logo (attached company logo)
• I don't have a bigger version for our company logo, but I have one old one, so you can remove the word from it)
• - insert the attached small PDGQ logo & RQC logo
• - creative, simple and clear business card.
• - Max. three colours
Nice to have
• - Here are the samples I would like to share with you: http://www.velmorindex.com/blog/minimalistic-business-card-designs/
• I would like to have my business card like one of the creation.
Should not have
• TBA

```html
<!DOCTYPE html>
<html lang="en">
<head>
<meta charset="utf-8">
<title>Kestrel + Design Ltd — Business Card</title>
<link rel="stylesheet" href="https://fonts.googleapis.com/css2?family=Source+Sans+3:wght@400;600;700&display=swap">
<style>
  :root {
    --bg: #e3e3e3;
    --halo: #e8e8e8;
    --card: #ffffff;
    --ink: #111111;
    --mark-dark: #4a4a4a;
    --mark-light: #f4f4f4;
    --mark-edge: #d2d2d2;
    --faint: #ececec;
    --shadow: rgba(0, 0, 0, 0.45);
  }
  * { margin: 0; padding: 0; box-sizing: border-box; }
  html, body { width: 1200px; height: 849px; overflow: hidden; }
  body {
    background: var(--bg);
    font-family: "Source Sans 3", Arial, sans-serif;
    color: var(--ink);
    position: relative;
  }
  .halo {
    position: absolute;
    left: 187px; top: 14px;
    width: 826px; height: 826px;
    border-radius: 50%;
    background: var(--halo);
  }
  .hero-mark {
    position: absolute;
    left: 440px; top: 200px;
    width: 320px; height: 56px;
    display: flex; align-items: center; justify-content: center; gap: 12px;
  }
  .hero-mark .dot {
    width: 22px; height: 22px; border-radius: 50%;
    background: var(--mark-light);
    border: 1px solid var(--mark-edge);
  }
  .hero-mark .name {
    font-size: 30px; font-weight: 600; color: var(--mark-light);
    text-shadow: none;
    -webkit-text-stroke: 0;
    letter-spacing: 0.5px;
  }
  .card {
    position: absolute;
    top: 392px;
    width: 344px; height: 221px;
    background: var(--card);
    border-radius: 21px;
    box-shadow: 4px 6px 9px var(--shadow);
    overflow: hidden;
  }
  .card--front { left: 204px; }
  .card--back { left: 618px; }
  .front-mark {
    position: absolute; inset: 0;
    display: flex; align-items: center; justify-content: center; gap: 8px;
  }
  .front-mark .dot {
    width: 12px; height: 12px; border-radius: 50%;
    background: var(--mark-dark);
  }
  .front-mark .name {
    font-size: 22px; font-weight: 600; color: var(--mark-dark);
  }
  .back-disc {
    position: absolute;
    left: -2px; top: 37px;
    width: 156px; height: 156px;
    border-radius: 50%;
    background: var(--faint);
  }
  .back-content {
    position: absolute;
    left: 0; right: 0; top: 32px;
    text-align: center;
  }
  .back-mark {
    display: flex; align-items: center; justify-content: center; gap: 5px;
    height: 26px;
  }
  .back-mark .dot {
    width: 7px; height: 7px; border-radius: 50%;
    background: var(--mark-dark);
  }
  .back-mark .name {
    font-size: 12px; font-weight: 600; color: var(--mark-dark);
  }
  .company {
    margin-top: 14px;
    font-size: 14.5px; font-weight: 700; line-height: 1;
  }
  .role {
    margin-top: 4px;
    font-size: 6.5px; font-weight: 600; line-height: 1;
  }
  .person {
    margin-top: 10px;
    font-size: 11px; font-weight: 400; line-height: 1;
  }
  .contacts {
    list-style: none;
    margin-top: 9px;
    font-size: 10px; font-weight: 600; line-height: 14px;
  }
  .badge {
    position: absolute;
    right: 15px; bottom: 15px;
    width: 26px; height: 26px;
    border-radius: 50%;
    background: var(--ink);
    border: 2px solid var(--mark-dark);
  }
</style>
</head>
<body>
  <div class="halo"></div>

  <div class="hero-mark">
    <span class="dot"></span>
    <span class="name">kestrel + design</span>
  </div>

  <section class="card card--front" aria-label="Card front">
    <div class="front-mark">
      <span class="dot"></span>
      <span class="name">kestrel + design</span>
    </div>
  </section>

  <section class="card card--back" aria-label="Card back">
    <div class="back-disc"></div>
    <div class="back-content">
      <div class="back-mark">
        <span class="dot"></span>
        <span class="name">kestrel + design</span>
      </div>
      <p class="company">kestrel + design Ltd.</p>
      <p class="role">architectural designer &amp; Design RQC</p>
      <p class="person">Mark Telford</p>
      <ul class="contacts">
        <li>mark@kdstudio.co.nz</li>
        <li>02 5319 6620</li>
        <li>www.kdstudio.co.nz</li>
      </ul>
    </div>
    <div class="badge" role="img" aria-label="Membership badge"></div>
  </section>
</body>
</html>
```